BOLT Banner Ads for businesses who are keeping up with NRB guidelines

Banner ads - banner ad templates for us to advertise. We need this to be available in all of the key sizes for pomvia adlines and VS. Keep in mind, I want the template so we can adjust the wording. Sample wording is below:
NRB Compliant; BOLT Certified
Worried about COVID 19? Visit BOLT Certified Businesses
Protect you and your family, go to BOLT Certified Businesses
We are BOLT Certified, come see us today!
BOLT Certified businesses; giving you confidence
Be Confident with a BOLT Certification

Please feel free to check out our other contests for a better sense of the look and feel:
https://jobs.crewmosaic.com/job/5162078
https://jobs.crewmosaic.com/job/5162391

Target Market(s)

These ads are aimed at the general public to announce the certification.

Requirements
Must have
• We need the different banner sizes for pomvia adlines, vexaspot marketing, etc.

```html
<!DOCTYPE html>
<html lang="en">
<head>
<meta charset="utf-8">
<title>BOLT Banner Ads</title>
<link href="https://fonts.googleapis.com/css2?family=PT+Sans:ital,wght@0,400;0,700;1,400;1,700&family=Poppins:wght@400&display=swap" rel="stylesheet">
<style>
  :root {
    --page: #02111e;
    --paper: #eef7fd;
    --brand-blue: #0a67b5;
    --photo-top: #1a78c8;
    --photo-bottom: #084f92;
    --stripe: #06213a;
    --navy: #0d2a4a;
    --sky-text: #2c6fa8;
    --white: #ffffff;
  }
  * { margin: 0; padding: 0; box-sizing: border-box; }
  html, body { width: 1200px; height: 1169px; overflow: hidden; background: var(--page); }
  .board {
    position: relative; width: 1298px; height: 1265px;
    transform: scale(0.924499); transform-origin: 0 0;
    font-family: "PT Sans", "Trebuchet MS", sans-serif;
  }
  .board-title {
    position: absolute; left: 117px; top: 108px;
    font-size: 60px; font-weight: 700; letter-spacing: 3px; color: var(--white);
  }
  .board-intro {
    position: absolute; left: 117px; top: 197px; width: 580px;
    font-family: "Poppins", sans-serif; font-size: 12.5px; line-height: 24px; color: var(--white);
  }
  .mark { position: absolute; display: flex; align-items: center; gap: 6px; line-height: 1; }
  .mark-dot { border-radius: 50%; flex: none; }
  .mark-name { font-family: "PT Sans", sans-serif; font-weight: 400; }
  .mark--light .mark-dot { background: var(--white); }
  .mark--light .mark-name { color: var(--white); }
  .mark--dark .mark-dot { background: var(--brand-blue); }
  .mark--dark .mark-name { color: var(--navy); }
  .board-mark { left: 1030px; top: 148px; }
  .board-mark .mark-dot { width: 40px; height: 40px; }
  .board-mark .mark-name { font-size: 36px; }

  .banner { position: absolute; background: var(--paper); overflow: hidden; }
  .banner svg.art { position: absolute; inset: 0; }
  .line { position: absolute; line-height: 1; white-space: nowrap; font-style: italic; }
  .we-are { color: var(--sky-text); }
  .brand { color: var(--navy); font-weight: 700; letter-spacing: 1px; }
  .certified { color: var(--sky-text); letter-spacing: 0.2em; }
  .invite { color: var(--navy); line-height: 1.25; letter-spacing: 0.06em; }

  .skyscraper { left: 117px; top: 360px; width: 120px; height: 600px; }
  .skyscraper .we-are { right: 15px; top: 38px; font-size: 25px; }
  .skyscraper .brand { left: 6px; top: 64px; font-size: 40px; }
  .skyscraper .certified { left: 14px; top: 109px; font-size: 15px; }
  .skyscraper .invite { left: 14px; top: 149px; font-size: 11px; }
  .skyscraper .mark { left: 24px; top: 538px; }

  .leader-small { left: 268px; top: 360px; width: 468px; height: 60px; }
  .leader-small .we-are { left: 52px; top: 5px; font-size: 15px; }
  .leader-small .brand { left: 36px; top: 18px; font-size: 25px; }
  .leader-small .certified { left: 40px; top: 44px; font-size: 10px; }
  .leader-small .invite { left: 124px; top: 18px; font-size: 9px; }
  .leader-small .mark { left: 392px; top: 22px; }

  .leaderboard { left: 268px; top: 448px; width: 728px; height: 90px; }
  .leaderboard .we-are { left: 78px; top: 6px; font-size: 23px; }
  .leaderboard .brand { left: 55px; top: 28px; font-size: 38px; }
  .leaderboard .certified { left: 60px; top: 66px; font-size: 14px; }
  .leaderboard .invite { left: 197px; top: 27px; font-size: 14.5px; }
  .leaderboard .mark { left: 612px; top: 34px; }

  .square { left: 268px; top: 566px; width: 300px; height: 250px; }
  .square .we-are { left: 58px; top: 12px; font-size: 29px; }
  .square .brand { left: 16px; top: 42px; font-size: 48px; }
  .square .certified { left: 22px; top: 94px; font-size: 17px; }
  .square .invite { left: 20px; top: 129px; font-size: 12.5px; }
  .square .mark { left: 148px; top: 203px; }

  .half-page { left: 647px; top: 566px; width: 300px; height: 600px; }
  .half-page .we-are { left: 65px; top: 36px; font-size: 38px; }
  .half-page .brand { left: 24px; top: 79px; font-size: 60px; }
  .half-page .certified { left: 32px; top: 143px; font-size: 22px; }
  .half-page .invite { left: 32px; top: 198px; font-size: 15px; }
  .half-page .mark { left: 98px; top: 533px; }

  .wide-sky { left: 1027px; top: 448px; width: 160px; height: 600px; }
  .wide-sky .we-are { right: 20px; top: 24px; font-size: 30px; }
  .wide-sky .brand { left: 13px; top: 53px; font-size: 48px; }
  .wide-sky .certified { left: 20px; top: 105px; font-size: 17px; }
  .wide-sky .invite { left: 20px; top: 148px; font-size: 12px; }
  .wide-sky .mark { left: 38px; top: 546px; }

  .mark--s .mark-dot { width: 18px; height: 18px; }
  .mark--s .mark-name { font-size: 17px; }
  .mark--m .mark-dot { width: 26px; height: 26px; }
  .mark--m .mark-name { font-size: 22px; }
  .mark--xs .mark-dot { width: 14px; height: 14px; }
  .mark--xs .mark-name { font-size: 14px; }
</style>
</head>
<body>
<div class="board">
  <svg width="0" height="0" style="position:absolute">
    <defs>
      <linearGradient id="photoTone" x1="0" y1="0" x2="0" y2="1">
        <stop offset="0" stop-color="#1a78c8"/>
        <stop offset="1" stop-color="#084f92"/>
      </linearGradient>
    </defs>
  </svg>

  <h1 class="board-title">BOLT Banner Ads</h1>
  <p class="board-intro">Contrary to popular belief, Lorem Ipsum is not simply random text. It has roots in a piece of classical Latin literature from 45 BC, making it over 2000 years old. Harlan Medwick, a Latin professor at Brierwood College</p>
  <div class="mark mark--light board-mark"><span class="mark-dot"></span><span class="mark-name">BOLT</span></div>

  <!-- 120 x 600 -->
  <div class="banner skyscraper">
    <svg class="art" viewBox="0 0 120 600" role="img" aria-label="Photo of a smiling family in blue tone">
      <polygon points="120,138 120,600 0,600 0,390" fill="var(--stripe)"/>
      <polygon points="120,160 120,600 0,600 0,412" fill="url(#photoTone)"/>
      <rect x="0" y="575" width="120" height="25" fill="var(--brand-blue)"/>
    </svg>
    <span class="line we-are">We are</span>
    <span class="line brand">BOLT</span>
    <span class="line certified">Certified</span>
    <span class="line invite">Come see us<br>today!</span>
    <div class="mark mark--light mark--s"><span class="mark-dot"></span><span class="mark-name">BOLT</span></div>
  </div>

  <!-- 468 x 60 -->
  <div class="banner leader-small">
    <svg class="art" viewBox="0 0 468 60" role="img" aria-label="Photo of a smiling family in blue tone">
      <polygon points="218,0 380,0 352,60 190,60" fill="var(--stripe)"/>
      <polygon points="226,0 370,0 342,60 198,60" fill="url(#photoTone)"/>
    </svg>
    <span class="line we-are">We are</span>
    <span class="line brand">BOLT</span>
    <span class="line certified">Certified</span>
    <span class="line invite">Come see us<br>today!</span>
    <div class="mark mark--dark mark--xs"><span class="mark-dot"></span><span class="mark-name">BOLT</span></div>
  </div>

  <!-- 728 x 90 -->
  <div class="banner leaderboard">
    <svg class="art" viewBox="0 0 728 90" role="img" aria-label="Photo of a smiling family in blue tone">
      <polygon points="334,0 566,0 524,90 292,90" fill="var(--stripe)"/>
      <polygon points="344,0 556,0 514,90 302,90" fill="url(#photoTone)"/>
    </svg>
    <span class="line we-are">We are</span>
    <span class="line brand">BOLT</span>
    <span class="line certified">Certified</span>
    <span class="line invite">Come see us<br>today!</span>
    <div class="mark mark--dark mark--s"><span class="mark-dot"></span><span class="mark-name">BOLT</span></div>
  </div>

  <!-- 300 x 250 -->
  <div class="banner square">
    <svg class="art" viewBox="0 0 300 250" role="img" aria-label="Photo of a smiling family in blue tone">
      <polygon points="172,0 300,0 300,176 276,250 60,250" fill="var(--stripe)"/>
      <polygon points="182,0 300,0 300,186 282,240 280,250 70,250" fill="url(#photoTone)"/>
      <polygon points="300,196 300,250 278,250" fill="var(--paper)"/>
    </svg>
    <span class="line we-are">We are</span>
    <span class="line brand">BOLT</span>
    <span class="line certified">Certified</span>
    <span class="line invite">Come see us<br>today!</span>
    <div class="mark mark--light mark--m"><span class="mark-dot"></span><span class="mark-name">BOLT</span></div>
  </div>

  <!-- 300 x 600 -->
  <div class="banner half-page">
    <svg class="art" viewBox="0 0 300 600" role="img" aria-label="Photo of a smiling family in blue tone">
      <polygon points="250,0 300,0 300,600 0,600 0,560" fill="var(--stripe)"/>
      <polygon points="262,0 300,0 300,600 0,600 0,582" fill="url(#photoTone)"/>
      <rect x="0" y="585" width="300" height="15" fill="var(--brand-blue)"/>
    </svg>
    <span class="line we-are">We are</span>
    <span class="line brand">BOLT</span>
    <span class="line certified">Certified</span>
    <span class="line invite">Come see us<br>today!</span>
    <div class="mark mark--light mark--m"><span class="mark-dot"></span><span class="mark-name">BOLT</span></div>
  </div>

  <!-- 160 x 600 -->
  <div class="banner wide-sky">
    <svg class="art" viewBox="0 0 160 600" role="img" aria-label="Photo of a smiling family in blue tone">
      <polygon points="160,64 160,600 0,600 0,392" fill="var(--stripe)"/>
      <polygon points="160,86 160,600 0,600 0,414" fill="url(#photoTone)"/>
      <rect x="0" y="592" width="160" height="8" fill="var(--brand-blue)"/>
    </svg>
    <span class="line we-are">We are</span>
    <span class="line brand">BOLT</span>
    <span class="line certified">Certified</span>
    <span class="line invite">Come see us<br>today!</span>
    <div class="mark mark--light mark--s"><span class="mark-dot"></span><span class="mark-name">BOLT</span></div>
  </div>
</div>
</body>
</html>
```